Retail Jewelry Business Card Design Project

We are in need of a new business card design for a retail jewelry store. This store is in the business of fine jewelry including but not specific to bridal jewelry, diamonds, designer jewelry and watches.

This store has been in business for 20 years but continues to strive for a modern professional appeal. The main colors use for this business are a royal blue, white and silver.

Target Market(s)

Target market is ages 18-50

Industry/Entity Type

Jewelry

Requirements
Must have
• Sales Person Name
Sales Person Email Address

Store Address
Store Phone
Website

Standard business card size. No odd shapes or sizes.
Nice to have
• Overall modern feel for card.

We have thought that a design with a nice feature of the logo on the back of the card would be nice but open to ideas.
Should not have
• No specific images of jewelry should be used.

```html
<!DOCTYPE html>
<html lang="en">
<head>
<meta charset="utf-8">
<title>Marcus Hale Fine Jewelry – Business Cards</title>
<link href="https://fonts.googleapis.com/css2?family=Open+Sans:ital,wght@0,400;0,600;1,700&display=swap" rel="stylesheet">
<style>
  :root {
    --royal: #2b3190;
    --lavender: #7470b6;
    --white: #ffffff;
    --ink: #333333;
    --ink-dark: #1e1e2a;
    --stage: #e9e9ec;
  }
  * { margin: 0; padding: 0; box-sizing: border-box; }
  html, body { width: 1200px; height: 788px; overflow: hidden; }
  body {
    background: var(--stage);
    font-family: "Open Sans", Arial, sans-serif;
    position: relative;
  }
  .label {
    position: absolute;
    width: 525px;
    text-align: center;
    font-size: 21px;
    color: var(--ink-dark);
  }
  .card {
    position: absolute;
    width: 525px;
    height: 300px;
    border-radius: 20px;
    overflow: hidden;
    box-shadow: 0 4px 12px rgba(0,0,0,.25);
  }
  .card--front  { left: 55px;  top: 73px;  background: var(--white); }
  .card--back-1 { left: 622px; top: 74px;  background: var(--white); }
  .card--back-2 { left: 54px;  top: 446px; background: var(--royal); }
  .card--back-3 { left: 622px; top: 446px; background: var(--lavender); }

  .swoosh { position: absolute; left: 0; top: 0; }
  .holder-name {
    position: absolute; left: 22px; top: 32px;
    color: var(--white); font-size: 16px;
  }
  .brand {
    position: absolute;
    color: var(--royal);
    font-weight: 600;
    text-align: center;
    line-height: 1.1;
  }
  .brand__name { display: block; }
  .brand__line { display: block; letter-spacing: .12em; text-transform: uppercase; }

  .card--front .brand { right: 24px; top: 70px; width: 230px; }
  .card--front .brand__name { font-size: 32px; }
  .card--front .brand__line { font-size: 14px; margin-top: 6px; }

  .contact {
    position: absolute; right: 22px; top: 184px;
    text-align: right; font-size: 13px; color: var(--ink);
    line-height: 24px; list-style: none;
  }
  .contact b { font-weight: 700; font-style: italic; }

  .card--back .brand { left: 0; right: 0; top: 72px; }
  .card--back .brand__name { font-size: 54px; }
  .card--back .brand__line { font-size: 20px; margin-top: 10px; }
  .card--back-2 .brand { color: var(--white); }
  .card--back-3 .brand { color: var(--royal); }

  .website {
    position: absolute; left: 0; right: 0; top: 258px;
    text-align: center; font-size: 13px; letter-spacing: .14em;
  }
  .card--back-1 .website { color: var(--royal); }
  .card--back-2 .website { color: var(--white); }
  .card--back-3 .website { color: var(--ink-dark); }
</style>
</head>
<body>
  <div class="label" style="left:55px; top:32px;">Front</div>
  <div class="label" style="left:622px; top:32px;">Back - 1</div>
  <div class="label" style="left:54px; top:403px;">Back - 2</div>
  <div class="label" style="left:622px; top:403px;">Back - 3</div>

  <section class="card card--front">
    <svg class="swoosh" width="525" height="300" viewBox="0 0 525 300" aria-hidden="true">
      <path d="M0,0 H390 Q160,55 0,198 Z" fill="var(--royal)"/>
      <path d="M0,206 Q170,62 412,0 H462 Q200,62 0,222 Z" fill="var(--lavender)"/>
    </svg>
    <p class="holder-name">Marcus Hale Brenton</p>
    <div class="brand">
      <span class="brand__name">Marcus Hale</span>
      <span class="brand__line">Fine Jewelry</span>
    </div>
    <ul class="contact">
      <li><b>phone</b> : 555-214-7730</li>
      <li><b>email</b> : marcus@marcushalejewelry.com</li>
      <li><b>web</b> : www.marcushalejewelry.com</li>
      <li>2280 Lindell Street, Bayport, FL 32507</li>
    </ul>
  </section>

  <section class="card card--back card--back-1">
    <div class="brand">
      <span class="brand__name">Marcus Hale</span>
      <span class="brand__line">Fine Jewelry</span>
    </div>
    <p class="website">www.marcushalejewelry.com</p>
  </section>

  <section class="card card--back card--back-2">
    <div class="brand">
      <span class="brand__name">Marcus Hale</span>
      <span class="brand__line">Fine Jewelry</span>
    </div>
    <p class="website">www.marcushalejewelry.com</p>
  </section>

  <section class="card card--back card--back-3">
    <div class="brand">
      <span class="brand__name">Marcus Hale</span>
      <span class="brand__line">Fine Jewelry</span>
    </div>
    <p class="website">www.marcushalejewelry.com</p>
  </section>
</body>
</html>
```